ZAMO needs a beautiful/corp web page

We are a pump an compressor repair facility in Alberta Canada. We love clean looks. white yellows greens blues. main page should involve conola fields, sun shine

Reason: i will be guaranteeing the project keep up the good work

Requirements
Must have
• open conola fields

```html
<!DOCTYPE html>
<html lang="en">
<head>
<meta charset="utf-8">
<title>ZAMO – Pump &amp; Compressor Repair</title>
<link rel="stylesheet" href="https://fonts.googleapis.com/css2?family=Lato:wght@300;400;700&family=Open+Sans:wght@400;600&display=swap">
<style>
:root{
  --yellow:#f7c600;
  --ink:#2b2b2b;
  --text:#3a3a3a;
  --rule:#e2e2e2;
  --white:#ffffff;
  --footer:#3a3a3a;
  --footer-dark:#2e2e2e;
  --footer-text:#b9b9b9;
  --footer-rule:#4c4c4c;
  --sky:#b9d3ea;
  --field:#f2d21a;
}
*{margin:0;padding:0;box-sizing:border-box}
html,body{width:960px;height:1200px;overflow:hidden}
body{position:relative;background:#f4f4f4;font-family:"Open Sans",Arial,sans-serif;color:var(--text)}
.backdrop{position:absolute;left:0;top:0;width:960px;height:944px;
  background:linear-gradient(180deg,#dbe8f3 0%,var(--sky) 14%,#e6eef2 22%,#e9dc5a 28%,var(--field) 40%,#e7c80f 60%,#b9b63a 80%,#d8c71b 100%)}
.page{position:absolute;left:136px;top:0;width:682px}

.brand{position:absolute;left:0;width:682px;top:60px;display:flex;align-items:center;justify-content:center;gap:10px}
.brand-dot{width:20px;height:20px;border-radius:50%;background:var(--yellow)}
.brand-name{font-family:"Lato",sans-serif;font-weight:700;font-size:28px;letter-spacing:1px;color:var(--ink)}

.nav{position:absolute;top:118px;left:0;width:682px;height:60px;background:var(--white);border-top:2px solid #d6e2ee;
  display:flex;justify-content:center;align-items:center;gap:28px}
.nav a{font-family:"Lato",sans-serif;font-weight:300;font-size:14.5px;color:#333;text-decoration:none}
.chev{display:inline-block;width:7px;height:10px;margin-right:5px;vertical-align:-1px}

.hero{position:absolute;top:197px;left:0;width:682px;height:249px;background:linear-gradient(180deg,#fafafa,#e2e2e2);overflow:hidden}
.hero-visual{position:absolute;left:284px;top:35px;width:398px;height:214px;
  background:linear-gradient(100deg,#eeeeee 0%,#c9ccd8 30%,#aeb6d8 50%,#d9dadf 75%,#ecdcd0 100%)}
.hero-title{position:absolute;left:35px;top:62px;font-family:"Open Sans",sans-serif;font-weight:400;font-size:36px;line-height:37px;color:#333;letter-spacing:-.3px}
.hero-title .accent{color:var(--yellow)}
.dots{position:absolute;right:44px;top:13px;display:flex;gap:5px}
.dots span{width:7px;height:7px;border-radius:50%;background:var(--yellow)}
.dots span+span{opacity:.7}

.content{position:absolute;top:456px;left:0;width:682px;height:488px;background:var(--white)}
.col{position:absolute;top:44px;width:176px}
.heading{font-family:"Lato",sans-serif;font-weight:300;font-size:14.5px;color:#333;padding-bottom:14px;border-bottom:1px solid var(--rule);margin-bottom:13px}
.lead{font-size:8.6px;font-weight:600;letter-spacing:.6px;line-height:13.6px;margin-bottom:13px;text-align:justify}
.body{font-size:8.6px;letter-spacing:.6px;line-height:13.6px;text-align:justify}
.btn{font-family:"Open Sans",sans-serif;font-size:9px;padding:3px 7px;text-decoration:none}
.btn-dark{background:#2b2b2b;color:#fff}
.btn-yellow{background:var(--yellow);color:#222}
.col .btn{display:table;margin:14px auto 0}

.divider{position:absolute;left:0;top:233px;width:682px;height:1px;background:var(--rule)}
.methods{position:absolute;left:38px;top:268px;width:392px}
.methods .lead{font-weight:400;color:#222;text-align:left}
.methods .body{text-align:left}
.methods .btn{display:table;margin:20px 4px 0 auto}

.video-col{position:absolute;left:468px;top:268px;width:177px}
.player{width:177px;height:112px;background:linear-gradient(180deg,#2a2a2a,#3b3b3b 60%,#1e1e1e);position:relative}
.player .bar{position:absolute;left:0;bottom:0;width:100%;height:8px;background:#111;border-top:1px solid #555}
.player svg{position:absolute;left:60px;top:23px}

.footer{position:absolute;top:944px;left:0;width:682px;height:216px;
  background:radial-gradient(ellipse at 50% 0%,#4a4a4a,var(--footer) 60%,var(--footer-dark));color:var(--footer-text)}
.fcol{position:absolute;top:32px;width:176px}
.fhead{font-family:"Lato",sans-serif;font-weight:300;font-size:14.5px;color:#fff;padding-bottom:14px;border-bottom:1px solid var(--footer-rule);margin-bottom:16px}
.fhead em{font-style:normal;color:var(--yellow)}
.flist{font-family:"Lato",sans-serif;font-weight:300;font-size:10px;line-height:12.6px;height:68px;border-bottom:1px solid var(--footer-rule)}
.fcol .btn{display:inline-block;margin-top:16px}
.social{display:flex;gap:32px;padding:11px 0 0 10px;height:84px;border-bottom:1px solid var(--footer-rule)}
.social span{width:28px;height:28px;border-radius:50%;background:#222;display:flex;align-items:center;justify-content:center}
.copy{display:flex;justify-content:space-between;align-items:center;margin-top:14px;font-family:"Lato",sans-serif;font-size:8px}
.copy b{font-family:"Lato",sans-serif;font-weight:700;font-size:11px;color:#ddd}
.shade{position:absolute;top:1160px;left:0;width:682px;height:40px;background:linear-gradient(180deg,#dcdcdc,#f4f4f4)}
</style>
</head>
<body>
<div class="backdrop" role="img" aria-label="Open canola field in full yellow bloom under a bright blue summer sky"></div>
<div class="page">
  <div class="brand"><span class="brand-dot"></span><span class="brand-name">ZAMO</span></div>

  <nav class="nav">
    <a href="#"><svg class="chev" viewBox="0 0 7 10"><path d="M1 1l4 4-4 4" stroke="#f7c600" stroke-width="2" fill="none"/></svg>ABOUT</a>
    <a href="#"><svg class="chev" viewBox="0 0 7 10"><path d="M1 1l4 4-4 4" stroke="#f7c600" stroke-width="2" fill="none"/></svg>SERVICES</a>
    <a href="#"><svg class="chev" viewBox="0 0 7 10"><path d="M1 1l4 4-4 4" stroke="#f7c600" stroke-width="2" fill="none"/></svg>CONTACT</a>
  </nav>

  <section class="hero">
    <div class="hero-visual" role="img" aria-label="Photo of a blue hard hat resting on engineering blueprints beside a measuring tape"></div>
    <h1 class="hero-title">Better<br>Maintainance,<br><span class="accent">Better Value</span></h1>
    <div class="dots"><span></span><span></span><span></span></div>
  </section>

  <main class="content">
    <div class="col" style="left:38px">
      <h2 class="heading"><svg class="chev" viewBox="0 0 7 10"><path d="M1 1l4 4-4 4" stroke="#f7c600" stroke-width="2" fill="none"/></svg> OUR PLEDGE</h2>
      <p class="lead">Quisque ultricies leo id felis porttitor eu sagittis orci imperdiet.</p>
      <p class="body">Nulla vitae odio quis massa condimentum venenatis. Quisque ultricies leo id felis porttitor eu sagittis orci imperdiet.</p>
      <a class="btn btn-dark" href="#">READ MORE</a>
    </div>
    <div class="col" style="left:254px">
      <h2 class="heading"><svg class="chev" viewBox="0 0 7 10"><path d="M1 1l4 4-4 4" stroke="#f7c600" stroke-width="2" fill="none"/></svg> OUR SERVICE</h2>
      <p class="lead">Nulla vitae odio quis massa condim entum venenatis.</p>
      <p class="body">Quisque ultricies leo id felis porttitor eu sagittis orci imperdiet. Nulla vitae odio quis massa condimentum venenatis.</p>
      <a class="btn btn-dark" href="#">READ MORE</a>
    </div>
    <div class="col" style="left:469px">
      <h2 class="heading"><svg class="chev" viewBox="0 0 7 10"><path d="M1 1l4 4-4 4" stroke="#f7c600" stroke-width="2" fill="none"/></svg> SOLUTIONS</h2>
      <p class="lead">Quisque ultricies leo id felis porttitor eu sagittis orci imperdiet.</p>
      <p class="body">Nulla vitae odio quis massa condimentum venenatis. Ut fermentum felis et massa sodales sit amet auctor urna pulvinar.</p>
      <a class="btn btn-dark" href="#">READ MORE</a>
    </div>

    <div class="divider"></div>

    <div class="methods">
      <h2 class="heading"><svg class="chev" viewBox="0 0 7 10"><path d="M1 1l4 4-4 4" stroke="#f7c600" stroke-width="2" fill="none"/></svg> PROVEN METHODS</h2>
      <p class="lead">Duis fringilla dapibus justo, ut congue ligula venenatis sed. In euismod risus eget mi vestibulum a interdum sem commodo.</p>
      <p class="body">Quisque ultricies leo id felis porttitor eu sagittis orci imperdiet. Nulla vitae odio quis massa condimentum venenatis. Ut fermentum felis et massa sodales sit amet auctor urna pulvinar. In faucibus neque egestas ipsum lacinia lacinia.</p>
      <a class="btn btn-yellow" href="#">READ MORE</a>
    </div>

    <div class="video-col">
      <h2 class="heading"><svg class="chev" viewBox="0 0 7 10"><path d="M1 1l4 4-4 4" stroke="#f7c600" stroke-width="2" fill="none"/></svg> OUR VIDEO</h2>
      <div class="player">
        <svg width="56" height="56" viewBox="0 0 56 56"><circle cx="28" cy="28" r="27" fill="#1c1c1c" stroke="#555"/><circle cx="28" cy="28" r="21" fill="#3a3a3a"/><path d="M23 18l13 10-13 10z" fill="#fff"/></svg>
        <div class="bar"></div>
      </div>
    </div>
  </main>

  <footer class="footer">
    <div class="fcol" style="left:38px">
      <h3 class="fhead"><em>//</em> ABOUT</h3>
      <p class="flist">- The most creative ideas<br>- Professional researches<br>- Precise and impartial approach<br>- Providing best solutions</p>
      <a class="btn btn-yellow" href="#">READ MORE</a>
    </div>
    <div class="fcol" style="left:254px">
      <h3 class="fhead"><em>//</em> CONTACT</h3>
      <p class="flist">48 Prairie Road<br>Red Deer, AB T4N 1A1<br>E-mail: hello@zamopumpworks.ca<br>Telephone: +1 800 555 0142</p>
      <a class="btn btn-yellow" href="#">CONTACT US</a>
    </div>
    <div class="fcol" style="left:469px">
      <h3 class="fhead"><em>//</em> SHARE</h3>
      <div class="social">
        <span aria-label="Share link"></span>
        <span aria-label="Share link"></span>
        <span aria-label="Email"><svg width="14" height="10" viewBox="0 0 14 10"><rect x="0.5" y="0.5" width="13" height="9" fill="#888"/><path d="M0.5 0.5l6.5 5 6.5-5" stroke="#222" fill="none"/></svg></span>
      </div>
      <div class="copy"><span>© 2013 Zamo Rotating Solutions</span><b>ZAMO</b></div>
    </div>
  </footer>
  <div class="shade"></div>
</div>
</body>
</html>
```